Looking for copywriting of the entire website + new selection of pictures

Hello,
My website's copy write is on the weaker side, so I'm looking for an entire re-do of my website's copy write. If you think a line is weak, re-write, otherwise you can leave it as is. We want our site to clearly explain what our events are, how they work, and why someone should sign up for them, while appealing to the hopeful, romantic, and nostalgic feelings of the visitors. Our speed dating events can be imagined as a modern day approach to the old-fashioned way of dating, where people got to know each other in person, away from the dating apps!! Additionally, I feel nearly all the existing pictures are rather weak, so please select entirely new pictures which give the website a less amateur feel, while retaining the playful nature of the brand. If there are areas where you think that section would benefit from no pictures at all, please communicate that.
Let me know if there are any further questions and thank you!
You can find the site at:
https://www.larkspindate.com
Industry/Entity Type
Speed Dating/Romance
Number of Pages Required
1 page
Look and feel
Each slider illustrates characteristics of the customer's brand and the style your logo design should communicate.

```html
<!DOCTYPE html>
<html lang="en">
<head>
<meta charset="utf-8">
<title>Larkspin Dating</title>
<link href="https://fonts.googleapis.com/css2?family=Playfair+Display:wght@400;600;700&family=Lato:wght@400;700&display=swap" rel="stylesheet">
<style>
:root{
  --pink:#f9c8da;
  --ornament:#e3aec1;
  --ink:#111111;
  --night:#121212;
  --white:#ffffff;
  --line:#d9d9d9;
  --serif:'Playfair Display', Georgia, serif;
  --sans:'Lato', Arial, sans-serif;
}
*{box-sizing:border-box;margin:0;padding:0}
html,body{width:1200px;height:4655px;overflow:hidden}
body{position:relative;background:var(--white);color:var(--ink);font-family:var(--sans)}
.abs{position:absolute}
.serif{font-family:var(--serif)}
.ornament{position:absolute;width:74px;height:26px;border-radius:13px;background:var(--ornament)}
.ornament.center{left:563px}
.section-title{position:absolute;left:0;width:1200px;text-align:center;font-family:var(--serif);font-weight:600;font-size:40px;line-height:1.1}
.btn{position:absolute;display:flex;align-items:center;justify-content:center;font-family:var(--serif);font-weight:600;font-size:14px;border-radius:6px;white-space:nowrap}

/* hero */
.hero{position:absolute;left:0;top:0;width:1200px;height:640px;background:linear-gradient(160deg,#3a1a14 0%,#7a2e1d 35%,#c1502a 60%,#e88a3c 78%,#2a140e 100%)}
.brand{left:110px;top:52px;color:var(--white);font-family:var(--serif);font-weight:600;font-size:24px}
.menu-btn{left:882px;top:57px;width:116px;height:42px;background:var(--white);color:var(--ink);font-size:13px}
.burger{left:1052px;top:64px}
.hero-kicker{left:110px;top:212px;color:var(--white);font-family:var(--serif);font-size:20px}
.hero-title{left:110px;top:250px;color:var(--white);font-family:var(--serif);font-weight:600;font-size:58px;line-height:1.1}
.hero-copy{left:110px;top:340px;color:var(--white);font-size:15px;white-space:nowrap}
.hero-list{left:110px;top:368px;list-style:none;color:var(--white);font-size:14px}
.hero-list li{display:flex;align-items:center;gap:10px;height:34px;white-space:nowrap}
.ghost{top:456px;height:40px;border:2px solid var(--white);color:var(--white)}
.solid-w{top:456px;height:40px;background:var(--white);color:var(--ink)}

/* locations */
.pill{position:absolute;top:810px;height:54px;background:var(--pink);display:flex;align-items:center;justify-content:center;font-family:var(--serif);font-weight:600;font-size:16px;border-radius:4px}

/* single */
.single-photo{left:110px;top:946px;width:468px;height:358px;border-radius:12px 0 0 12px;background:linear-gradient(135deg,#e9e6e2,#bdb6ae 60%,#8a8078)}
.single-bar{left:578px;top:946px;width:511px;height:68px;background:var(--pink);padding-left:79px;display:flex;align-items:center;font-family:var(--serif);font-weight:600;font-size:20px}
.single-copy{left:657px;top:1030px;font-size:17px;line-height:55px;white-space:nowrap}

/* newsletter */
.news{left:0;top:1395px;width:1200px;height:640px;background:var(--pink);border-radius:0 0 60px 0}
.news-copy{left:0;width:1200px;top:1672px;text-align:center;font-size:18px}
.news-btn{left:514px;top:1735px;width:140px;height:46px;background:var(--white);box-shadow:0 2px 10px rgba(0,0,0,.1)}

/* how */
.how-copy{left:110px;top:2147px;font-size:14px;line-height:38px;list-style:none;white-space:nowrap}
.how-copy .sub{padding-left:10px}
.how-copy .two{line-height:22px;padding:8px 0}
.how-photo{left:620px;top:2049px;width:468px;height:468px;border-radius:12px;background:radial-gradient(circle at 50% 45%,#b2765a,#5a3528 55%,#2a1812)}

/* band */
.band{left:0;top:2610px;width:1200px;height:352px;background:var(--pink)}
.band-copy{left:140px;width:920px;top:2676px;text-align:center;font-family:var(--serif);font-weight:600;font-size:20px;line-height:43px;color:var(--ink)}
.dark-btn{top:2838px;height:46px;background:var(--ink);color:var(--white);font-size:13px}

/* casual */
.card{position:absolute;top:3153px;width:272px;height:226px;border-radius:12px;display:flex;flex-direction:column;align-items:center;justify-content:center;gap:18px;font-family:var(--serif);font-weight:600;font-size:23px;text-align:center}
.card.dark{background:var(--ink);color:var(--white)}
.card.light{background:var(--pink);color:var(--ink)}

/* faq */
.faq{position:absolute;left:110px;width:978px;height:68px;border:2px solid var(--line);border-radius:34px;display:flex;align-items:center;padding:0 24px;font-size:19px}
.faq .q{flex:1;padding-left:16px}
.faq .plus{width:26px;height:26px;background:var(--ink);border-radius:4px;display:flex;align-items:center;justify-content:center}
.more{left:510px;top:4204px;width:180px;height:46px;background:var(--ink);color:var(--white)}

/* footer */
.footer{left:0;top:4322px;width:1200px;height:333px;background:var(--night)}
.foot-brand{left:110px;top:4480px;font-family:var(--serif);font-weight:600;font-size:30px;color:var(--white)}
.foot-nav{top:4400px;font-family:var(--serif);font-weight:600;font-size:14px;color:var(--white)}
.foot-line{font-family:var(--serif);font-weight:600;font-size:14px;color:var(--white);display:flex;align-items:center;gap:10px}
.dot{width:14px;height:14px;border-radius:50%;background:var(--white)}
</style>
</head>
<body>

<header class="hero" role="img" aria-label="Couple holding hands in silhouette against a glowing sunset sky"></header>
<div class="abs brand">Larkspin Dating</div>
<div class="btn menu-btn">Contact Us</div>
<svg class="abs burger" width="38" height="28" viewBox="0 0 38 28"><g stroke="#fff" stroke-width="3" stroke-linecap="round"><line x1="10" y1="4" x2="36" y2="4"/><line x1="2" y1="14" x2="36" y2="14"/><line x1="10" y1="24" x2="36" y2="24"/></g></svg>
<div class="abs hero-kicker">Put the phone down. Pull up a chair.</div>
<h1 class="abs hero-title">Larkspin Dating</h1>
<p class="abs hero-copy">Old-fashioned romance, reimagined as speed dating for today.</p>
<ul class="abs hero-list">
  <li><svg width="14" height="12" viewBox="0 0 14 12"><path d="M7 12L1 6A3.3 3.3 0 0 1 7 2a3.3 3.3 0 0 1 6 4z" fill="#fff"/></svg>No hosts, no name tags, just easy, honest conversation</li>
  <li><svg width="14" height="12" viewBox="0 0 14 12"><path d="M7 12L1 6A3.3 3.3 0 0 1 7 2a3.3 3.3 0 0 1 6 4z" fill="#fff"/></svg>Pick an evening → meet someone in person</li>
</ul>
<div class="btn solid-w" style="left:110px;width:134px">How It Works</div>
<div class="btn ghost" style="left:266px;width:116px">Our Events</div>

<section>
  <div class="ornament center" style="top:697px" role="img" aria-label="Small hearts ornament"></div>
  <h2 class="section-title" style="top:738px">Where We Meet</h2>
  <div class="pill" style="left:110px;width:184px">BOSTON, MA</div>
  <div class="pill" style="left:353px;width:217px">PHILADELPHIA, PA</div>
  <div class="pill" style="left:630px;width:183px">JERSEY CITY, NJ</div>
  <div class="pill" style="left:872px;width:217px">NEW YORK CITY, NY</div>
</section>

<section>
  <div class="abs single-photo" role="img" aria-label="Young woman on a sofa looking at her phone"></div>
  <div class="abs single-bar">Tired of swiping?</div>
  <div class="abs single-copy">
    <p>Remember when meeting someone felt like magic?</p>
    <p>Larkspin Dating brings that feeling back.</p>
    <p>Real chemistry across a coffee-shop table.</p>
    <p>Choose a night near you and say hello.</p>
  </div>
</section>

<section>
  <div class="abs news" role="img" aria-label="Soft pink watercolor wash"></div>
  <div class="ornament center" style="top:1553px" role="img" aria-label="Small hearts ornament"></div>
  <h2 class="section-title" style="top:1594px">Seats Go Quickly. Save Yours Early.</h2>
  <p class="abs news-copy">Get our monthly letter with every upcoming event in your city.</p>
  <div class="btn news-btn">Join the List</div>
</section>

<section>
  <div class="ornament" style="left:110px;top:2050px" role="img" aria-label="Small hearts ornament"></div>
  <h2 class="abs serif" style="left:108px;top:2090px;font-weight:600;font-size:40px;line-height:1.1">How It Works</h2>
  <ul class="abs how-copy">
    <li>No hosts, no name tags - just the way dating used to feel</li>
    <li>Your evening, step by step:</li>
    <li>♥ Arrive at your chosen venue at your set time</li>
    <li>♥ Watch for a personal text guiding you through the night:</li>
    <li class="sub">- When each round begins and ends</li>
    <li class="sub">- A short note on who you’ll meet next</li>
    <li>♥ Spot your date, take a seat, and let the talk flow!</li>
    <li class="two">♥ When the round ends, text back whether it’s<br>&nbsp;&nbsp;a Match (M) or a Pass (P)</li>
    <li>♥ Repeat, relax, and enjoy the night!</li>
  </ul>
  <div class="abs how-photo" role="img" aria-label="Smiling couple sharing a moment by candlelight"></div>
</section>

<section>
  <div class="abs band"></div>
  <p class="abs band-copy">Every evening brings 7 rounds of 10 minutes each. Long enough to find a spark, share a laugh, and feel whether the chemistry is real. No scripted small talk and no pressure, just the honest, face-to-face conversation that great stories begin with.</p>
  <div class="btn dark-btn" style="left:246px;width:141px">7 Rounds</div>
  <div class="btn dark-btn" style="left:451px;width:142px">7 Dates</div>
  <div class="btn dark-btn" style="left:648px;width:307px">7 Chances at something new</div>
</section>

<section>
  <div class="ornament center" style="top:3040px" role="img" aria-label="Small hearts ornament"></div>
  <h2 class="section-title" style="top:3072px">Easygoing Is Our Style</h2>
  <div class="card dark" style="left:110px">
    <svg width="56" height="66" viewBox="0 0 56 66" fill="none" stroke="#f9c8da" stroke-width="3" stroke-linejoin="round"><path d="M20 4v12l-6 10h28l-6-10V4M14 26L4 60h48L42 26"/></svg>
    Come as You Are</div>
  <div class="card light" style="left:465px">
    <svg width="60" height="50" viewBox="0 0 60 50" fill="none" stroke="#111" stroke-width="3"><path d="M10 4h40a6 6 0 0 1 6 6v20a6 6 0 0 1-6 6H24l-12 10v-10h-2a6 6 0 0 1-6-6V10a6 6 0 0 1 6-6z"/><line x1="18" y1="16" x2="42" y2="16"/><line x1="18" y1="24" x2="36" y2="24"/></svg>
    Honest Conversation</div>
  <div class="card dark" style="left:818px">
    <svg width="64" height="56" viewBox="0 0 64 56" fill="none" stroke="#f9c8da" stroke-width="3"><circle cx="18" cy="12" r="8"/><circle cx="46" cy="12" r="8"/><path d="M4 52V36a10 10 0 0 1 10-10h8a10 10 0 0 1 10 10v16H4zM32 52V36a10 10 0 0 1 10-10h8a10 10 0 0 1 10 10v16H32z"/></svg>
    Relaxed Dates</div>
</section>

<section>
  <div class="ornament center" style="top:3472px" role="img" aria-label="Small hearts ornament"></div>
  <h2 class="section-title" style="top:3504px">Your Questions, Answered</h2>
  <div class="faq" style="top:3580px"><svg width="20" height="14" viewBox="0 0 20 14"><path d="M1 7h17M12 1l6 6-6 6" stroke="#111" stroke-width="2" fill="none"/></svg><span class="q">What should I know before I arrive?</span><span class="plus"><svg width="12" height="12"><path d="M6 1v10M1 6h10" stroke="#fff" stroke-width="2"/></svg></span></div>
  <div class="faq" style="top:3666px"><svg width="20" height="14" viewBox="0 0 20 14"><path d="M1 7h17M12 1l6 6-6 6" stroke="#111" stroke-width="2" fill="none"/></svg><span class="q">What if I need to cancel or can’t make it?</span><span class="plus"><svg width="12" height="12"><path d="M6 1v10M1 6h10" stroke="#fff" stroke-width="2"/></svg></span></div>
  <div class="faq" style="top:3752px"><svg width="20" height="14" viewBox="0 0 20 14"><path d="M1 7h17M12 1l6 6-6 6" stroke="#111" stroke-width="2" fill="none"/></svg><span class="q">How many people will I meet?</span><span class="plus"><svg width="12" height="12"><path d="M6 1v10M1 6h10" stroke="#fff" stroke-width="2"/></svg></span></div>
  <div class="faq" style="top:3838px"><svg width="20" height="14" viewBox="0 0 20 14"><path d="M1 7h17M12 1l6 6-6 6" stroke="#111" stroke-width="2" fill="none"/></svg><span class="q">How long does each date last?</span><span class="plus"><svg width="12" height="12"><path d="M6 1v10M1 6h10" stroke="#fff" stroke-width="2"/></svg></span></div>
  <div class="faq" style="top:3924px"><svg width="20" height="14" viewBox="0 0 20 14"><path d="M1 7h17M12 1l6 6-6 6" stroke="#111" stroke-width="2" fill="none"/></svg><span class="q">What happens when a date ends?</span><span class="plus"><svg width="12" height="12"><path d="M6 1v10M1 6h10" stroke="#fff" stroke-width="2"/></svg></span></div>
  <div class="faq" style="top:4010px"><svg width="20" height="14" viewBox="0 0 20 14"><path d="M1 7h17M12 1l6 6-6 6" stroke="#111" stroke-width="2" fill="none"/></svg><span class="q">I felt a spark with someone. What’s next?</span><span class="plus"><svg width="12" height="12"><path d="M6 1v10M1 6h10" stroke="#fff" stroke-width="2"/></svg></span></div>
  <div class="faq" style="top:4096px"><svg width="20" height="14" viewBox="0 0 20 14"><path d="M1 7h17M12 1l6 6-6 6" stroke="#111" stroke-width="2" fill="none"/></svg><span class="q">Is there a pause between dates?</span><span class="plus"><svg width="12" height="12"><path d="M6 1v10M1 6h10" stroke="#fff" stroke-width="2"/></svg></span></div>
  <div class="btn more">See All Questions</div>
</section>

<footer class="abs footer"></footer>
<div class="abs foot-brand">Larkspin Dating</div>
<span class="abs foot-nav" style="left:450px">Home</span>
<span class="abs foot-nav" style="left:560px">Event Locations</span>
<span class="abs foot-nav" style="left:740px">How it Works</span>
<span class="abs foot-nav" style="left:903px">FAQ</span>
<span class="abs foot-nav" style="left:1002px">Contact Us</span>
<div class="abs foot-line" style="left:450px;top:4450px">
  <svg width="14" height="11" viewBox="0 0 14 11"><rect x="0.5" y="0.5" width="13" height="10" fill="#fff"/><path d="M1 1l6 5 6-5" stroke="#121212" fill="none"/></svg>welcome@larkspindate.com
  <span style="width:30px"></span>
  <svg width="12" height="12" viewBox="0 0 12 12"><path d="M2 0l3 3-1.5 1.5a8 8 0 0 0 4 4L9 7l3 3-2 2C5 12 0 7 0 2z" fill="#fff"/></svg>(201) 555-0148
</div>
<div class="abs foot-line" style="left:450px;top:4498px">Copyright © 2023 Larkspin Dating. All rights reserved.</div>
<div class="abs foot-line" style="left:450px;top:4547px;gap:26px"><span class="dot"></span><span class="dot"></span><span class="dot"></span></div>

</body>
</html>
```